(4) Bowling League Designs 1920x1080

Will be used on our website and in some digital signage.

We are starting (4) leagues this summer and need a basic graphic as an attention grab which will then lead the customer to full information / sign ups. The information I would need on each one is as follows:

1. Monday Night FREE ball league - Begins May 3rd

2. Tuesday Trios - NPTA Sanctioned - Begins May 11th
$9,000 prize fund

3. Wednesday Cosmic League - 9 pin no tap fun league - May 12th start

4. Thursday Night FREE ball league - Begins May 13th

I will attach some random examples of previous ones to give you an idea.

```html
<!DOCTYPE html>
<html lang="en">
<head>
<meta charset="utf-8">
<title>Monday Night Free Ball League</title>
<link rel="stylesheet" href="https://fonts.googleapis.com/css2?family=Bebas+Neue&display=swap">
<style>
  :root {
    --ink-dark: #120807;
    --amber: #f4a33e;
    --white: #ffffff;
    --accent-red: #e0322a;
    --lane-tan: #c9975a;
    --glow-orange: #ff9a2e;
    --dusk-purple: #4a1f5c;
  }
  html, body {
    margin: 0;
    padding: 0;
    width: 1200px;
    height: 675px;
    overflow: hidden;
    background: var(--ink-dark);
  }
  .league-banner {
    position: relative;
    width: 1200px;
    height: 675px;
    overflow: hidden;
    font-family: "Bebas Neue", "Arial Narrow", sans-serif;
  }
  .alley-scene {
    position: absolute;
    inset: 0;
    background:
      radial-gradient(circle at 1180px 20px, rgba(255,220,150,0.95) 0, rgba(255,150,40,0.6) 60px, transparent 260px),
      radial-gradient(ellipse 190px 200px at 600px 330px, #4a4548 0, #2a2628 60%, transparent 100%),
      radial-gradient(ellipse 420px 120px at 560px 140px, rgba(200,120,110,0.35) 0, transparent 100%),
      radial-gradient(ellipse 700px 260px at 800px 560px, rgba(214,162,96,0.9) 0, rgba(150,95,50,0.5) 55%, transparent 100%),
      radial-gradient(ellipse 500px 300px at 60px 640px, rgba(74,31,92,0.9) 0, transparent 100%),
      linear-gradient(100deg, #160a08 0%, #2a130c 35%, #5a2a12 65%, #a8521c 100%);
  }
  .headline {
    position: absolute;
    left: 0;
    top: 0;
    margin: 0;
    font-weight: 400;
    line-height: 1;
  }
  .headline span { display: block; position: absolute; white-space: nowrap; text-shadow: 0 2px 8px rgba(0,0,0,0.45); }
  .line-day { left: 158px; top: 166px; font-size: 164px; }
  .line-league { left: 158px; top: 304px; font-size: 160px; }
  .line-start { left: 162px; top: 449px; font-size: 94px; letter-spacing: 1px; }
  .amber { color: var(--amber); }
  .white { color: var(--white); }
  .accent-rules { position: absolute; inset: 0; pointer-events: none; }
</style>
</head>
<body>
  <main class="league-banner">
    <div class="alley-scene" role="img" aria-label="Bowling ball rolling down a polished wooden lane toward pins under warm lights"></div>
    <svg class="accent-rules" width="1200" height="675" viewBox="0 0 1200 675" aria-hidden="true">
      <defs>
        <linearGradient id="rule-fade" x1="0" x2="1">
          <stop offset="0" stop-color="#e0322a" stop-opacity="0.9"/>
          <stop offset="0.5" stop-color="#ff5a30" stop-opacity="1"/>
          <stop offset="1" stop-color="#e0322a" stop-opacity="0.7"/>
        </linearGradient>
        <radialGradient id="flare">
          <stop offset="0" stop-color="#fff6d8"/>
          <stop offset="0.3" stop-color="#ffb040" stop-opacity="0.8"/>
          <stop offset="1" stop-color="#ff7a20" stop-opacity="0"/>
        </radialGradient>
      </defs>
      <line x1="160" y1="318" x2="1032" y2="241" stroke="url(#rule-fade)" stroke-width="2.5"/>
      <ellipse cx="575" cy="278" rx="110" ry="10" fill="url(#flare)"/>
      <line x1="160" y1="551" x2="612" y2="511" stroke="url(#rule-fade)" stroke-width="2.5"/>
    </svg>
    <h1 class="headline">
      <span class="line-day"><span class="amber" style="position:static;display:inline">Monday</span> <span class="white" style="position:static;display:inline">Night</span></span>
      <span class="line-league"><span class="white" style="position:static;display:inline">Free Ball</span> <span class="amber" style="position:static;display:inline">League</span></span>
      <span class="line-start"><span class="amber" style="position:static;display:inline">Begins</span> <span class="white" style="position:static;display:inline">May 3rd</span></span>
    </h1>
  </main>
</body>
</html>
```